New Letterhead request for our Law Firm!

We are a small Estate Planning Firm who just got out logo redesigned. It's attached. We need some letterhead for our client welcome letters and so forth. Clean, bright, and approachable is our style. If you need the specifications for our color scheme or other versions of the logo file, we have those too. Visit our website to get an idea about our services/aesthetics:https://bramblecove.law/

Target Market(s)

Adults 30-80

Colors

Designer to choose colors to be used in the design.

Requirements
Must have
• Logo with color. Contact information

```html
<!DOCTYPE html>
<html lang="en">
<head>
<meta charset="utf-8">
<title>Bramble Cove Law Firm – Letterhead</title>
<link rel="stylesheet" href="https://fonts.googleapis.com/css2?family=Open+Sans:wght@400;600&display=swap">
<style>
  :root {
    --backdrop: #ebebeb;
    --paper: #ffffff;
    --sage: #6b9a84;
    --sage-soft: #a9c8b8;
    --charcoal: #3d3e42;
    --slate: #8a8b8f;
    --ink: #505154;
  }
  * { margin: 0; padding: 0; box-sizing: border-box; }
  html, body {
    width: 1200px;
    height: 794px;
    overflow: hidden;
    background: var(--backdrop);
    font-family: "Open Sans", Arial, sans-serif;
  }
  .stage {
    width: 1200px;
    height: 794px;
    display: flex;
    align-items: center;
    justify-content: center;
  }
  .letterhead {
    position: relative;
    width: 530px;
    height: 750px;
    background: var(--paper);
    box-shadow: 0 2px 10px rgba(0, 0, 0, 0.08);
  }
  .brand {
    position: absolute;
    top: 44px;
    left: 44px;
    display: flex;
    align-items: center;
    gap: 10px;
  }
  .brand-dot {
    width: 30px;
    height: 30px;
    border: 2px solid var(--sage);
    border-radius: 50%;
  }
  .brand-name {
    color: var(--sage);
    font-weight: 600;
    font-size: 17px;
    letter-spacing: 1.5px;
    text-transform: uppercase;
  }
  .foliage {
    position: absolute;
    right: 0;
    bottom: 118px;
    width: 112px;
    height: 96px;
    background: linear-gradient(135deg, var(--sage-soft) 0%, #c9cacd 60%, var(--slate) 100%);
    opacity: 0.75;
    border-radius: 56px 0 0 56px;
  }
  .footer {
    position: absolute;
    left: 0;
    right: 0;
    bottom: 0;
  }
  .contact {
    padding: 0 44px 8px;
    display: flex;
    justify-content: space-between;
    align-items: flex-end;
    font-size: 9.5px;
    line-height: 1.45;
    color: var(--ink);
  }
  .contact .label { color: var(--sage); }
  .website { color: var(--ink); }
  .rule {
    height: 3px;
    background: var(--sage);
    margin-bottom: 4px;
  }
  .band {
    height: 32px;
    background: var(--charcoal);
  }
</style>
</head>
<body>
  <main class="stage">
    <article class="letterhead">
      <header class="brand">
        <span class="brand-dot"></span>
        <span class="brand-name">Bramble Cove Law Firm</span>
      </header>

      <div class="foliage" role="img" aria-label="Decorative tree branch with sage and grey leaves"></div>

      <footer class="footer">
        <div class="contact">
          <address class="address" style="font-style: normal;">
            Bramble Cove Law Firm, PLLC<br>
            420 Lakeview Parkway, Suite 110, Fernbrook, MN 55990<br>
            <span class="label">Tel :</span> 555 014 2297 <span class="label">Email :</span> info@bramblecove.law
          </address>
          <span class="website">www.bramblecove.law</span>
        </div>
        <div class="rule"></div>
        <div class="band"></div>
      </footer>
    </article>
  </main>
</body>
</html>
```